Website revision

I have a current website (www.tobarwendle.example) that I need to have revised. I am building a personal brand and I want it to look very professional. I built the current site and it has a lot of the elements already in place but the design is poor.

Target Market(s)

Busy working professionals that what to get in better shape

Industry/Entity Type

Health And Wellness

Number of Pages Required

1 page

Colors
00a990
9bcb3b

Requirements
Must have
• I want it re-designed with the Lumo Theme that I currently have. I want to make sure that all of my links remain active. I just need it to look more professional to my personal brand than it is at the moment.
Nice to have
• I want to appeal to a working professional that is short on time but still wants to stay healthy and fit. I am the guy that is going to provide the solution to them.
Should not have
• I do NOT want to look like a gym or a spa. I am appealing to working professionals.

```html
<!DOCTYPE html>
<html lang="en">
<head>
<meta charset="utf-8">
<title>Tobar Wendle – Your Holistic Lifestyle Coach</title>
<link href="https://fonts.googleapis.com/css2?family=Roboto+Condensed:wght@300;400;700&family=Open+Sans:wght@400;600&display=swap" rel="stylesheet">
<style>
:root{
  --teal:#00a990;
  --lime:#9bcb3b;
  --ink:#222;
  --muted:#666;
  --dark:#1c211e;
  --footer:#1e1e1e;
  --panel:#f2f2f2;
  --field:#f3f3f3;
  --white:#fff;
}
*{box-sizing:border-box;margin:0;padding:0}
html,body{width:1200px;height:4499px;overflow:hidden}
body{font-family:"Open Sans",sans-serif;color:var(--ink);background:var(--white);position:relative}
.abs{position:absolute}
.btn{position:absolute;background:var(--teal);color:var(--white);font-size:14px;display:flex;align-items:center;justify-content:center;text-decoration:none}
.heading{font-family:"Roboto Condensed",sans-serif;font-weight:300;letter-spacing:2px;color:var(--ink)}
.center{left:0;width:1200px;text-align:center}
.photo{position:absolute}

/* top bar */
.topbar{position:absolute;left:0;top:0;width:1200px;height:38px;background:var(--dark);color:var(--white);font-size:12px}
.topbar .item{position:absolute;top:11px;display:flex;align-items:center;gap:8px}
.social{position:absolute;top:0;display:flex}
.social span{width:38px;height:38px;display:flex;align-items:center;justify-content:center}
.social span i{width:12px;height:12px;background:var(--white);display:block;border-radius:2px}
.social span:first-child{background:var(--teal)}

/* header */
.header{position:absolute;left:0;top:38px;width:1200px;height:119px;border-bottom:1px solid #e5e5e5}
.brand{position:absolute;left:79px;top:30px;display:flex;align-items:center;gap:10px}
.brand .dot{width:46px;height:46px;border-radius:50%;background:#7a7f3a}
.brand .name{font-family:"Roboto Condensed",sans-serif;font-weight:700;font-size:28px;color:#7a7f3a;letter-spacing:0.5px}
.nav{position:absolute;right:79px;top:52px;display:flex;gap:34px;font-size:13px}
.nav a{color:var(--ink);text-decoration:none}
.nav a.active{color:var(--teal);border-bottom:2px solid var(--teal);padding-bottom:6px}

/* hero */
.hero{position:absolute;left:0;top:157px;width:1200px;height:542px;background:linear-gradient(90deg,#4a4d4c,#8c8f90 45%,#5b5e5e)}
.hero h1{position:absolute;left:79px;top:218px;font-family:"Roboto Condensed",sans-serif;font-weight:700;font-size:38px;line-height:44px;color:var(--white);letter-spacing:1px}
.optin{position:absolute;left:776px;top:128px;width:347px;height:330px;background:var(--lime);padding:26px 26px}
.optin h3{font-family:"Roboto Condensed",sans-serif;font-weight:700;font-size:19px;color:var(--white);text-align:center;line-height:22px;letter-spacing:1px;margin-bottom:14px}
.optin .field{height:42px;background:var(--white);margin-bottom:16px;font-size:13px;color:#555;padding:12px 20px}
.optin .send{height:42px;background:var(--teal);color:var(--white);font-size:14px;display:flex;align-items:center;justify-content:center}

/* about */
.about h2{position:absolute;left:81px;top:820px;font-size:38px}
.underline{position:absolute;height:2px;width:98px;background:var(--teal)}
.body-text{position:absolute;font-size:12.5px;line-height:17px;color:var(--muted)}
.play{position:absolute;left:857px;top:947px;width:56px;height:38px;background:#e02020;border-radius:9px}
.play::after{content:"";position:absolute;left:22px;top:11px;border-left:15px solid var(--white);border-top:8px solid transparent;border-bottom:8px solid transparent}

/* courses */
.card-title{position:absolute;top:1626px;width:328px;text-align:center;font-family:"Roboto Condensed",sans-serif;font-weight:700;font-size:19px;letter-spacing:0.5px;white-space:nowrap}

/* guide */
.guide{position:absolute;left:0;top:1789px;width:1200px;height:510px;background:var(--panel)}
.guide h2{position:absolute;left:79px;top:96px;font-size:38px;line-height:44px}

/* blogs */
.blog{position:absolute;top:2428px;width:327px;height:423px;background:var(--white);box-shadow:0 0 14px rgba(0,0,0,.08)}
.blog .img{position:absolute;left:0;top:0;width:327px;height:221px}
.blog .date{position:absolute;right:10px;top:167px;width:170px;height:42px;background:var(--teal);color:var(--white);font-size:14px;display:flex;align-items:center;justify-content:center}
.blog .meta{position:absolute;left:22px;top:244px;font-size:12px;color:var(--muted)}
.blog h4{position:absolute;left:22px;top:270px;width:290px;font-size:14.5px;line-height:19px;color:var(--teal);font-weight:600}
.blog p{position:absolute;left:22px;top:326px;width:290px;font-size:12px;line-height:17px;color:var(--muted)}
.blog .more{position:absolute;left:22px;top:385px;font-size:12.5px;color:var(--muted);text-decoration:underline}

/* stories */
.arrow{position:absolute;top:2977px;width:30px;height:30px;border-radius:50%;display:flex;align-items:center;justify-content:center}
.stories{position:absolute;left:96px;top:3084px;width:1008px;height:606px;background:var(--panel)}
.frame{position:absolute;top:3127px;height:428px;background:var(--white);padding:10px}
.frame .photo{position:relative;width:100%;height:100%}
.tab{position:absolute;top:3260px;width:46px;height:168px;background:var(--teal);color:var(--white);font-family:"Roboto Condensed",sans-serif;font-weight:700;font-size:26px;letter-spacing:2px;display:flex;align-items:center;justify-content:center}
.tab span{transform:rotate(-90deg);white-space:nowrap}
.story{position:absolute;left:419px;top:3127px;width:360px;height:428px;background:var(--white);padding:28px 24px}
.story h3{font-family:"Roboto Condensed",sans-serif;font-weight:400;font-size:29px;letter-spacing:2px;margin-bottom:14px}
.story .rule{height:1px;background:#e3e3e3;margin-bottom:20px}
.story p{font-size:12.5px;line-height:17px;color:var(--muted);margin-bottom:20px}

/* contact */
.input{position:absolute;background:var(--field);font-size:11px;color:#999;padding:14px 18px}

/* footer */
.footer{position:absolute;left:0;top:4109px;width:1200px;height:390px;background:var(--footer);color:#ddd}
.footer h5{position:absolute;top:76px;font-family:"Roboto Condensed",sans-serif;font-weight:400;font-size:19px;color:var(--white);letter-spacing:0.5px}
.footer ul{position:absolute;list-style:none;font-size:12.5px;line-height:24px}
.footer li::before{content:"›";margin-right:12px}
.contact-list li::before{content:none}
.contact-list li{display:flex;gap:12px;align-items:flex-start;line-height:22px}
.contact-list svg{margin-top:5px;flex:none}
.subscribe{position:absolute;left:854px;top:191px;width:266px;height:44px;background:var(--white);display:flex}
.subscribe span{flex:1;font-size:12.5px;color:#333;padding:13px 14px}
.subscribe b{width:50px;background:var(--teal);display:flex;align-items:center;justify-content:center}
.copy{position:absolute;left:0;top:328px;width:1200px;border-top:1px solid #3a3a3a}
.fsocial{position:absolute;right:79px;top:348px;display:flex;gap:8px}
.fsocial i{width:30px;height:30px;border-radius:50%;background:var(--white);display:block}
.fsocial i:first-child{background:var(--teal)}
</style>
</head>
<body>

<div class="topbar">
  <div class="item" style="left:79px">
    <svg width="13" height="13" viewBox="0 0 24 24"><path fill="#fff" d="M6.6 10.8a15 15 0 0 0 6.6 6.6l2.2-2.2c.3-.3.7-.4 1-.2 1.1.4 2.3.6 3.6.6.6 0 1 .4 1 1V20c0 .6-.4 1-1 1A17 17 0 0 1 3 4c0-.6.4-1 1-1h3.5c.6 0 1 .4 1 1 0 1.3.2 2.5.6 3.6.1.3 0 .7-.2 1z"/></svg>
    <span>000 555 010 2040</span>
  </div>
  <div class="item" style="left:524px">
    <svg width="18" height="12" viewBox="0 0 18 12"><rect x="0.5" y="0.5" width="17" height="11" fill="none" stroke="#fff"/><path d="M1 1l8 6 8-6" fill="none" stroke="#fff"/></svg>
    <span>info@tobarwendle.example</span>
  </div>
  <div class="social" style="left:937px">
    <span><i></i></span><span><i></i></span><span><i></i></span><span><i></i></span><span><i></i></span>
  </div>
</div>

<header class="header">
  <div class="brand"><div class="dot"></div><div class="name">TOBAR WENDLE</div></div>
  <nav class="nav">
    <a class="active" href="#">Home</a><a href="#">About</a><a href="#">Courses &amp; Programs</a><a href="#">Blog</a><a href="#">Tobar in the Media</a><a href="#">Contact</a>
  </nav>
</header>

<section class="hero">
  <div class="photo" role="img" aria-label="Coach in a suit holding suspension training straps in a gym" style="left:0;top:0;width:1200px;height:542px;background:linear-gradient(90deg,#3d4140,#a8abab 48%,#4d5150)"></div>
  <h1>Let's Build a Healthy<br>Lifestyle Together...</h1>
  <a class="btn" href="#" style="left:79px;top:329px;width:169px;height:42px">Read More</a>
  <form class="optin">
    <h3>Yes! Send Me My Healthy Quick<br>Snack Guide!</h3>
    <div class="field">Name</div>
    <div class="field">Phone</div>
    <div class="field">Email</div>
    <div class="send">Send</div>
  </form>
</section>

<section class="about">
  <h2 class="heading">About Tobar Wendle...</h2>
  <div class="underline" style="left:81px;top:871px"></div>
  <p class="body-text" style="left:81px;top:910px;width:490px">Tobar Wendle has been a powerful contributor to the health and wellness space for over 20 years. As a published health author, Tobar is frequently interviewed on radio stations across the country and frequently speaks as a Keynote Speaker for various associations and corporations.</p>
  <a class="btn" href="#" style="left:81px;top:1010px;width:169px;height:44px">Read More</a>
  <div class="photo" role="img" aria-label="Video still of the coach standing in a gym with cardio machines" style="left:618px;top:804px;width:502px;height:333px;background:linear-gradient(135deg,#9a9d9b,#5f6462)"></div>
  <div class="play"></div>
</section>

<section class="courses">
  <h2 class="heading center abs" style="top:1190px;font-size:38px">Courses &amp; Programs</h2>
  <p class="body-text center" style="top:1249px;left:250px;width:700px;text-align:center">Thank you for visiting my courses page! At the moment my only "live" course is the Quick Stride Fitness Course (click below for details). Stay tuned for many more courses and services by signing up for my newsletter at the bottom of the page. Life is Good!</p>
  <div class="photo" role="img" aria-label="Course artwork with a running figure and the course name" style="left:79px;top:1328px;width:328px;height:276px;background:linear-gradient(135deg,#e2e2e2 55%,#e59a2a 55%)"></div>
  <div class="photo" role="img" aria-label="A word written in sugar above donuts and sweets" style="left:435px;top:1328px;width:328px;height:276px;background:linear-gradient(180deg,#ececec 40%,#c98b5a)"></div>
  <div class="photo" role="img" aria-label="Person holding out the waistband of loose jeans" style="left:792px;top:1328px;width:328px;height:276px;background:linear-gradient(180deg,#f2ddd0,#d7b3a0 45%,#3f5674)"></div>
  <div class="card-title" style="left:79px">Quick Stride Fitness Course</div>
  <div class="card-title" style="left:435px">Sweet Reset Course</div>
  <div class="card-title" style="left:792px">The Core Four Slim-Down Mini-Course</div>
  <a class="btn" href="#" style="left:512px;top:1691px;width:169px;height:44px">ViewMore</a>
</section>

<section class="guide">
  <h2 class="heading">Claim Your Free On-The-Go<br>Quick Snack Guide Today!</h2>
  <p class="body-text" style="left:79px;top:223px;width:510px">Do you ever get frustrated because you want to eat better but you are short on time? You have come to the right place! When you sign up for my newsletter I will send you a copy of my Quick &amp; Healthy Snack Guide which is loaded with over 45 healthy snacks. Don't be a victim of your tight schedule...download my snack guide today and enjoy better health with these convenient snacks!</p>
  <a class="btn" href="#" style="left:79px;top:349px;width:169px;height:44px">Read More</a>
  <div class="photo" role="img" aria-label="Snack guide book cover with fresh vegetables and the coach" style="left:690px;top:52px;width:337px;height:413px;background:linear-gradient(160deg,#d8d6b9,#8f9a4e 50%,#2d3b5a);transform:skewY(6deg)"></div>
</section>

<section class="blogs">
  <h2 class="heading center abs" style="top:2352px;font-size:34px">Blogs</h2>
  <article class="blog" style="left:79px">
    <div class="img" role="img" aria-label="Overhead view of bowls of superfood salads" style="background:linear-gradient(135deg,#6b5a4a,#a9946f 50%,#4f5b3a)"></div>
    <div class="date">Jun 10, 2019</div>
    <div class="meta">by Tobar Wendle &nbsp;|&nbsp; 2 comments</div>
    <h4>Superfoods That You Do Not Know Are Superfoods</h4>
    <p>In this short video I discuss the not-so-heard of superfoods that might be in your house right now</p>
    <a class="more" href="#">Read More</a>
  </article>
  <article class="blog" style="left:440px">
    <div class="img" role="img" aria-label="Feet standing on a bathroom scale" style="background:linear-gradient(180deg,#e9e6e1,#b9b3ab)"></div>
    <div class="date">Jun 10, 2019</div>
    <div class="meta">by Tobar Wendle &nbsp;|&nbsp; 2 comments</div>
    <h4>Eat Less Calories &amp; Lose Weight With This Simple Trick</h4>
    <p>"Tobar I feel SO full ever since I started eating the way that you want me too! Are you sure that I am not going to gain weight..</p>
    <a class="more" href="#">Read More</a>
  </article>
  <article class="blog" style="left:794px">
    <div class="img" role="img" aria-label="Soul vs Ego graphic with a fraying rope on a dark blue background" style="background:linear-gradient(180deg,#12163f,#2a3a8a)"></div>
    <div class="date">Jun 10, 2019</div>
    <div class="meta">by Tobar Wendle &nbsp;|&nbsp; 2 comments</div>
    <h4>The Hot Mess Inside Your Brain Is Screwing You Over Big Time</h4>
    <p>Have you ever felt like you were justified in not taking action towards your goals? Do you have another side of you that disagree's?</p>
    <a class="more" href="#">Read More</a>
  </article>
  <a class="btn" href="#" style="left:519px;top:2890px;width:169px;height:43px">View More</a>
</section>

<section class="success">
  <h2 class="heading center abs" style="top:2967px;font-size:34px">A Few of My Success Stories</h2>
  <div class="arrow" style="left:1046px;background:#333"><svg width="10" height="12" viewBox="0 0 10 12"><path d="M7 1L2 6l5 5" fill="none" stroke="#fff" stroke-width="2"/></svg></div>
  <div class="arrow" style="left:1089px;background:var(--teal)"><svg width="10" height="12" viewBox="0 0 10 12"><path d="M3 1l5 5-5 5" fill="none" stroke="#fff" stroke-width="2"/></svg></div>
  <p class="body-text" style="left:300px;top:3033px;width:600px;text-align:center">Fitness Lorem Ipsum is simply dummy text of the printing simply dummy and simply dummy typesetting industry.</p>
  <div class="stories"></div>
  <div class="frame" style="left:114px;width:286px"><div class="photo" role="img" aria-label="Before photo of the client standing in water" style="background:linear-gradient(180deg,#8a7a5a,#b98a6c 50%,#6d6648)"></div></div>
  <div class="story">
    <h3>Dale Marsh</h3>
    <div class="rule"></div>
    <p>% Fat : 20<br>% Fat : 8<br>Four Month<br>Transformation</p>
    <p>Dale is an Orthodontist that owns his own business, has 6 kids and is heavily involved in his church and enjoys biking.</p>
    <p>I was fortunate enough to help Dale understand how to incorporate weight training, food prep and sleep hygiene and more personal time into his hectic lifestyle.</p>
  </div>
  <div class="frame" style="left:798px;width:287px"><div class="photo" role="img" aria-label="After photo of the client in black and white" style="background:linear-gradient(180deg,#9a9a9a,#5c5c5c)"></div></div>
  <div class="tab" style="left:80px"><span>Before</span></div>
  <div class="tab" style="left:1073px"><span>After</span></div>
  <a class="btn" href="#" style="left:528px;top:3597px;width:169px;height:44px">View More</a>
</section>

<section class="contact">
  <h2 class="heading center abs" style="top:3734px;font-size:32px">Quick Contact</h2>
  <div class="input" style="left:203px;top:3791px;width:251px;height:44px">Name*</div>
  <div class="input" style="left:475px;top:3791px;width:252px;height:44px">Phone*</div>
  <div class="input" style="left:746px;top:3791px;width:253px;height:44px">Email*</div>
  <div class="input" style="left:203px;top:3854px;width:796px;height:112px">Message</div>
  <a class="btn" href="#" style="left:521px;top:3987px;width:169px;height:43px">Send</a>
</section>

<footer class="footer">
  <div class="brand" style="top:64px"><div class="dot"></div><div class="name">TOBAR WENDLE</div></div>
  <p style="position:absolute;left:79px;top:137px;width:220px;font-size:12.5px;line-height:16px;color:#ddd">Lorem Ipsum is simply dummy text of the printing and typesetting Lorem Ipsum is simply..</p>
  <a href="#" style="position:absolute;left:79px;top:190px;font-size:13px;color:#ddd">Read More</a>

  <h5 style="left:423px">Quick Link</h5>
  <ul style="left:425px;top:133px">
    <li>Home</li><li>About</li><li>Courses &amp; Programs</li><li>Blog</li><li>Tobar in the Media</li><li>Contact</li>
  </ul>

  <h5 style="left:634px">Quick Contact</h5>
  <ul class="contact-list" style="left:634px;top:134px;width:200px">
    <li><svg width="10" height="13" viewBox="0 0 10 13"><path d="M5 0a5 5 0 0 1 5 5c0 3.5-5 8-5 8S0 8.5 0 5a5 5 0 0 1 5-5zm0 3a2 2 0 1 0 0 4 2 2 0 0 0 0-4z" fill="#ddd"/></svg><span>48 Alder Row<br>Brookhaven Falls, USA<br>Zip :12345</span></li>
    <li><svg width="10" height="10" viewBox="0 0 24 24"><path fill="#ddd" d="M6.6 10.8a15 15 0 0 0 6.6 6.6l2.2-2.2c.3-.3.7-.4 1-.2 1.1.4 2.3.6 3.6.6.6 0 1 .4 1 1V20c0 .6-.4 1-1 1A17 17 0 0 1 3 4c0-.6.4-1 1-1h3.5c.6 0 1 .4 1 1 0 1.3.2 2.5.6 3.6.1.3 0 .7-.2 1z"/></svg><span>+000 555 0199</span></li>
    <li><svg width="11" height="8" viewBox="0 0 18 12"><rect width="18" height="12" fill="#ddd"/><path d="M1 1l8 6 8-6" fill="none" stroke="#1e1e1e"/></svg><span>info@tobarwendle.example</span></li>
  </ul>

  <h5 style="left:854px;font-size:22px;top:72px">Subscribe</h5>
  <p style="position:absolute;left:854px;top:133px;width:270px;font-size:12.5px;line-height:16px">Lorem Ipsum is simply dummy text printing and typesetting industry.</p>
  <div class="subscribe"><span>Email Address</span><b><svg width="18" height="18" viewBox="0 0 24 24"><path d="M2 11l20-9-7 20-3-8z" fill="#fff"/></svg></b></div>

  <div class="copy"></div>
  <p style="position:absolute;left:79px;top:354px;font-size:12.5px">© Copyright 2019 Tobar Wendle - All Right Reserved - Privacy &amp; Seurty</p>
  <div class="fsocial"><i></i><i></i><i></i><i></i><i></i></div>
</footer>

</body>
</html>
```